sailbrightly Website for children with diabilities

Hi, we are looking for a new website design for our community service "sailbrightly". Sailbrightly gives children who suffer from diseases or disabilities a week off on a Boat to give the children new hope and an unforgettable experience.

The current website is really old and we want to have a new one.
Please feel free to discover our website under http://sailbrightly-example.at/.
We have several company sponsors which are very important to us.

The Website has to be a Bootstrap Design (Version 4.4 or higher) [NOT Wordpress, Joomla, other CMS]

Target Market(s)

no target market. we like to inform our communities about our service.

Industry/Entity Type

community service for children with disabilities

Coding

Number of Pages Required

4 page

Font styles to use
Sans Serif

Colors
0054AA
0677BA
7BADD7
CADEEF
E8F1F8
0094D4
00A9DD
6FCCEA
C7EBF8
E9F6FB

Requirements
Must have
• About, Sponsors, Information about cruises
Nice to have
• Gallery

```html
<!DOCTYPE html>
<html lang="en">
<head>
<meta charset="utf-8">
<title>Sail Brightly</title>
<link rel="stylesheet" href="https://fonts.googleapis.com/css2?family=Poppins:wght@400;500;600&family=Rajdhani:wght@600;700&display=swap">
<style>
:root{
  --navy:#0f1b5c;
  --navy-deep:#070d2c;
  --blue:#0677BA;
  --blue-2:#0094D4;
  --blue-3:#00A9DD;
  --sky:#6FCCEA;
  --ice:#E9F6FB;
  --ink:#1c1c1c;
  --text:#3d3d3d;
  --faint:#e6e8ee;
}
*{margin:0;padding:0;box-sizing:border-box}
html,body{width:1200px;height:4789px;overflow:hidden}
body{font-family:"Poppins",sans-serif;color:var(--text);background:#fff;position:relative}
.abs{position:absolute}
.head{font-family:"Rajdhani",sans-serif;font-weight:700;text-transform:uppercase}
.btn{display:inline-block;font-family:"Rajdhani",sans-serif;font-weight:700;color:#fff;border-radius:30px;text-align:center}
.hl{color:var(--blue-2)}

/* top bar */
.topbar{top:0;left:0;width:1200px;height:50px;background:var(--blue);color:#fff;font-size:13px}
.topbar .dark{left:0;top:0;width:410px;height:50px;background:var(--navy);clip-path:polygon(0 0,100% 0,94% 100%,0 100%)}
.topbar .item{top:0;height:50px;display:flex;align-items:center;gap:10px;font-weight:500}
.dot{width:28px;height:28px;border-radius:50%;background:#fff;display:inline-block}
.ic{width:30px;height:30px;border-radius:50%;background:#fff;display:flex;align-items:center;justify-content:center}

/* hero */
.hero{top:50px;left:0;width:1200px;height:740px;background:linear-gradient(180deg,#5fb6e6 0%,#3a8fcf 45%,#1d4f8f 62%,#1a5fa5 100%)}
.nav{top:93px;left:111px;width:976px;height:52px;background:#fff;border-radius:30px;display:flex;align-items:center;padding-left:150px;gap:46px;font-size:15px;font-weight:500;color:var(--ink)}
.nav .active{color:var(--blue);border-bottom:2px solid var(--blue);padding-bottom:2px}
.nav .contact{position:absolute;right:14px;top:9px;background:var(--blue);color:#fff;border-radius:20px;padding:6px 18px;font-size:15px}
.logo{top:67px;left:110px;width:104px;height:104px;border-radius:50%;background:#fff;border:5px solid var(--navy);display:flex;align-items:center;justify-content:center;text-align:center;font-family:"Rajdhani",sans-serif;font-weight:700;font-size:17px;line-height:1;color:var(--navy)}
.hero-ring{left:116px;top:211px;width:370px;height:370px;border-radius:50%;background:rgba(6,119,186,.45)}
.hero-disc{left:145px;top:240px;width:312px;height:312px;border-radius:50%;background:rgba(6,119,186,.85);color:#fff;text-align:center;padding-top:38px}
.hero-disc .w{font-family:"Rajdhani",sans-serif;font-weight:600;font-size:36px}
.hero-disc .t{font-family:"Rajdhani",sans-serif;font-weight:700;font-size:54px;line-height:1}
.hero-disc p{font-size:14px;line-height:30px;margin:10px 24px 14px}
.hero-disc .btn{background:var(--navy);font-size:24px;padding:10px 26px}

/* section titles */
.ghost{left:0;width:1200px;text-align:center;font-size:64px;color:var(--faint);letter-spacing:2px}
.title{left:0;width:1200px;text-align:center;font-size:36px;color:var(--ink)}

/* about */
.lead{left:230px;width:740px;text-align:center;font-size:15px;line-height:29px;color:var(--ink)}
.side-label{left:102px;top:1200px;transform-origin:left top;transform:rotate(-90deg);font-size:18px;color:var(--ink);letter-spacing:1px;white-space:nowrap}
.side-line{left:118px;top:930px;width:2px;height:115px;background:#ccc}
.about-text{left:173px;top:922px;width:420px}
.about-text h3{font-size:32px;color:var(--ink);margin-bottom:14px}
.about-text p{font-size:15px;line-height:27px;color:var(--text)}
.ticks{list-style:none;margin-top:12px}
.ticks li{display:flex;align-items:center;gap:14px;font-size:15px;color:var(--ink);height:43px}
.about-text .btn{background:var(--blue-2);font-size:24px;padding:10px 26px;margin-top:20px;box-shadow:0 4px 10px rgba(0,0,0,.2)}
.pattern{left:1002px;top:1160px;width:198px;height:280px;background:var(--ice)}
.about-photo{left:665px;top:925px;width:416px;height:416px;border-radius:50%;border:12px solid var(--navy);background:linear-gradient(180deg,#8fb7dc,#5c6d7a 60%,#3b4a53)}

/* services */
.services{top:1440px;left:0;width:1200px;height:775px;background:linear-gradient(180deg,#1e2b7a,#1a2668)}
.services .ghost{color:rgba(255,255,255,.12)}
.services .title{color:#fff}
.card{top:1634px;width:279px;background:repeating-linear-gradient(135deg,#1f8fd8 0 6px,#1b86cf 6px 12px);border-radius:0 0 0 90px;color:#fff;text-align:center}
.card .icon{width:130px;height:130px;border-radius:50%;background:rgba(255,255,255,.3);margin:42px auto 20px;display:flex;align-items:center;justify-content:center}
.card .icon span{width:106px;height:106px;border-radius:50%;background:#fff;display:flex;align-items:center;justify-content:center}
.card h4{font-family:"Rajdhani",sans-serif;font-weight:700;font-size:22px;line-height:32px;margin:0 20px}
.card p{font-size:13px;line-height:26px;margin:6px 18px 8px}
.card .more{font-weight:600;font-size:17px}
.card.mid{background:repeating-linear-gradient(135deg,#1654b8 0 6px,#134fae 6px 12px);border-radius:0 0 0 90px}
.card .photo{height:160px;background:linear-gradient(180deg,#9ccbeb,#e2e6ea 60%,#c9d2da)}
.arrow{width:36px;height:36px;border-radius:50%;border:2px solid #fff;display:flex;align-items:center;justify-content:center}

/* cruises */
.cruise-photo{left:0;top:2396px;width:529px;height:497px;border-radius:0 260px 260px 0;background:linear-gradient(160deg,#b9a27c,#6d5d4c 50%,#2a3550)}
.cruise-text{left:589px;top:2404px;width:500px;font-size:15px;line-height:29px;color:var(--text)}
.thumb{top:2652px;width:108px;height:108px;border-radius:50%}
.track{left:589px;top:2789px;width:498px;height:4px;background:#cfcfcf}
.track span{position:absolute;left:139px;top:0;width:92px;height:4px;background:#555}

/* gallery */
.gallery{top:2980px;left:0;width:1200px;height:810px;background:linear-gradient(180deg,#2ea3e0,#1b95d8)}
.gallery .ghost{color:rgba(255,255,255,.18)}
.gallery .title{color:#fff}
.tile{position:absolute}
.brand-box{left:700px;top:3213px;width:331px;height:189px;background:var(--navy);color:#fff;text-align:center;padding-top:48px}
.brand-box .name{font-family:"Rajdhani",sans-serif;font-weight:700;font-size:40px}
.brand-box .follow{display:flex;justify-content:center;align-items:center;gap:10px;font-size:13px;margin-top:12px}

/* sponsors */
.sponsor{top:4063px;width:214px;height:119px;border-radius:16px;background:#fff;box-shadow:0 4px 14px rgba(0,0,0,.15);display:flex;align-items:center;justify-content:center;font-family:"Poppins",sans-serif;font-weight:600;font-size:22px;color:var(--navy)}
.sponsor.on{background:var(--navy);color:#fff}
.arrow.dark{border-color:var(--ink)}

/* footer */
.footer{top:4330px;left:0;width:1200px;height:459px;background:var(--navy-deep);color:#fff}
.fcol{top:4460px;font-size:15px}
.fcol h5{font-family:"Rajdhani",sans-serif;font-weight:600;font-size:26px;margin-bottom:12px}
.fcol li{list-style:none;height:34px;display:flex;align-items:center;gap:10px}
.chev{color:var(--blue-2);font-weight:600}
.flogo{left:784px;top:4480px;width:100px;height:100px;border-radius:50%;background:#fff;color:var(--navy);display:flex;align-items:center;justify-content:center;text-align:center;font-family:"Rajdhani",sans-serif;font-weight:700;font-size:16px;line-height:1}
.fcircle{width:28px;height:28px;border-radius:50%;background:var(--blue-2);display:inline-block}
</style>
</head>
<body>

<!-- top bar -->
<div class="abs topbar">
  <div class="abs dark"></div>
  <div class="abs item" style="left:110px">Follow Us On:
    <span class="dot" style="margin-left:6px"></span><span class="dot"></span><span class="dot"></span>
  </div>
  <div class="abs item" style="left:440px">
    <span class="ic"><svg width="16" height="16" viewBox="0 0 24 24"><path d="M6.6 10.8a15 15 0 006.6 6.6l2.2-2.2a1 1 0 011-.25 11 11 0 003.6.6 1 1 0 011 1V20a1 1 0 01-1 1A17 17 0 013 4a1 1 0 011-1h3.5a1 1 0 011 1 11 11 0 00.6 3.6 1 1 0 01-.25 1z" fill="#0677BA"/></svg></span>+1 555 014 2290
  </div>
  <div class="abs item" style="left:652px">
    <span class="ic"><svg width="14" height="16" viewBox="0 0 24 24"><path d="M12 2a7 7 0 00-7 7c0 5 7 13 7 13s7-8 7-13a7 7 0 00-7-7zm0 9.5A2.5 2.5 0 1112 6a2.5 2.5 0 010 5.5z" fill="#0677BA"/></svg></span>Sailbrightly, United States
  </div>
  <div class="abs item" style="left:904px">
    <span class="ic"><svg width="16" height="14" viewBox="0 0 24 24"><path d="M3 5h18v14H3z" fill="#0677BA"/><path d="M3 5l9 7 9-7" stroke="#fff" stroke-width="1.6" fill="none"/></svg></span>info@sailbrightly.com
  </div>
</div>

<!-- hero -->
<div class="abs hero" role="img" aria-label="Sailing yacht on open blue sea under a clear sky"></div>
<svg class="abs" style="left:0;top:640px" width="1200" height="160" viewBox="0 0 1200 160">
  <path d="M0 70 C250 40 400 100 650 115 C900 130 1050 80 1200 20 L1200 160 L0 160Z" fill="#7BADD7"/>
  <path d="M0 95 C250 60 420 115 650 125 C900 135 1050 90 1200 45 L1200 160 L0 160Z" fill="#0094D4"/>
  <path d="M0 118 C250 85 420 130 650 137 C900 145 1050 105 1200 70 L1200 160 L0 160Z" fill="#fff"/>
</svg>
<div class="abs nav">
  <span class="active">Home</span><span>About</span><span>Sponsors</span><span>Information About Cruises</span><span>Gallery</span>
  <span style="display:flex;align-items:center;gap:8px;margin-left:-16px">En
    <svg width="26" height="26" viewBox="0 0 26 26"><circle cx="13" cy="13" r="13" fill="#0677BA"/><circle cx="13" cy="13" r="7" stroke="#fff" stroke-width="1.4" fill="none"/><path d="M6 13h14M13 6c-3 4-3 10 0 14M13 6c3 4 3 10 0 14" stroke="#fff" stroke-width="1.2" fill="none"/></svg></span>
  <span class="contact">Contact Us</span>
</div>
<div class="abs logo">Sail<br>Brightly</div>
<div class="abs hero-ring"></div>
<div class="abs hero-disc">
  <div class="w">Welcome To</div>
  <div class="t">Sail Brightly</div>
  <p>The participants are consciously involved in sailing activities.</p>
  <span class="btn">Get Started</span>
</div>

<!-- about -->
<div class="abs head ghost" style="top:748px">About Sail Brightly</div>
<div class="abs head title" style="top:784px">About Sail Brightly</div>
<p class="abs lead" style="top:838px">The <span class="hl">participants</span> are consciously <span class="hl">involved</span> in sailing activities. There are <span class="hl">responsibilities</span> for a wide variety of <span class="hl">tasks in daily life</span>.</p>
<div class="abs side-line"></div>
<div class="abs head side-label">About Sail Brightly</div>
<div class="abs about-text">
  <h3 class="head">Here's About</h3>
  <p>This gives everyone the feeling of being important to the community and everyone learns to take on this responsibility if they can. Sail Brightly offers an ideal training ground for social learning.</p>
  <ul class="ticks">
    <li><svg width="22" height="18" viewBox="0 0 22 18"><path d="M2 9l6 6L20 2" stroke="#0094D4" stroke-width="3.4" fill="none"/></svg>Variety of tasks in daily life</li>
    <li><svg width="22" height="18" viewBox="0 0 22 18"><path d="M2 9l6 6L20 2" stroke="#0094D4" stroke-width="3.4" fill="none"/></svg>Involvement of every crew member</li>
    <li><svg width="22" height="18" viewBox="0 0 22 18"><path d="M2 9l6 6L20 2" stroke="#0094D4" stroke-width="3.4" fill="none"/></svg>Experiences can lead to self-esteem</li>
    <li><svg width="22" height="18" viewBox="0 0 22 18"><path d="M2 9l6 6L20 2" stroke="#0094D4" stroke-width="3.4" fill="none"/></svg>Ideal training ground for social learning</li>
  </ul>
  <span class="btn">Read More</span>
</div>
<div class="abs pattern" role="img" aria-label="Dotted decorative pattern"></div>
<div class="abs about-photo" role="img" aria-label="Group of children and volunteers at a marina"></div>

<!-- services -->
<div class="abs services" role="img" aria-label="Dark blue tinted photo of a harbour with sailing boats"></div>
<div class="abs head ghost" style="top:1508px;color:rgba(255,255,255,.12)">Our Services</div>
<div class="abs head title" style="top:1545px;color:#fff">Our Services</div>
<div class="abs arrow" style="left:36px;top:1850px"><svg width="16" height="14" viewBox="0 0 16 14"><path d="M15 7H2M7 1L1 7l6 6" stroke="#fff" stroke-width="2" fill="none"/></svg></div>
<div class="abs arrow" style="left:1130px;top:1850px"><svg width="16" height="14" viewBox="0 0 16 14"><path d="M1 7h13M9 1l6 6-6 6" stroke="#fff" stroke-width="2" fill="none"/></svg></div>

<div class="abs card" style="left:111px;height:465px">
  <div class="icon"><span><svg width="56" height="56" viewBox="0 0 56 56"><circle cx="28" cy="22" r="10" stroke="#222" stroke-width="2" fill="none"/><path d="M14 48c2-10 26-10 28 0" stroke="#222" stroke-width="2" fill="none"/></svg></span></div>
  <h4>Experiential Learning</h4>
  <p>Through the reflection and also the care afterwards in the individual facilities, the children and young people can draw on this experience for a long time to come.</p>
  <div class="more">Read More &raquo;</div>
</div>
<div class="abs card mid" style="left:461px;height:502px">
  <div class="photo" role="img" aria-label="Children in life jackets aboard a sailing yacht"></div>
  <div class="icon" style="margin:-60px auto 10px;width:84px;height:84px"><span style="width:72px;height:72px"><svg width="40" height="40" viewBox="0 0 40 40"><circle cx="20" cy="14" r="6" stroke="#222" stroke-width="2" fill="none"/><circle cx="8" cy="22" r="4" stroke="#222" stroke-width="2" fill="none"/><circle cx="32" cy="22" r="4" stroke="#222" stroke-width="2" fill="none"/><path d="M10 36c2-8 18-8 20 0" stroke="#222" stroke-width="2" fill="none"/></svg></span></div>
  <h4>Take Responsibility For Yourself And Others</h4>
  <p>The fact of steering a sailing ship alone fills many with great pride. Recurring activities on the ship require the involvement of every crew member.</p>
  <div class="more">Read More &raquo;</div>
</div>
<div class="abs card" style="left:810px;height:465px">
  <div class="icon"><span><svg width="56" height="56" viewBox="0 0 56 56"><circle cx="28" cy="28" r="16" stroke="#222" stroke-width="2" fill="none"/><circle cx="28" cy="28" r="6" stroke="#222" stroke-width="2" fill="none"/><path d="M28 8v6M28 42v6M8 28h6M42 28h6" stroke="#222" stroke-width="2"/></svg></span></div>
  <h4>Practicing Tolerance</h4>
  <p>Through the reflection and also the care afterwards in the individual facilities, the children and young people can draw on this experience for a long time to come.</p>
  <div class="more">Read More &raquo;</div>
</div>

<!-- cruises -->
<div class="abs head ghost" style="top:2270px">Information About Cruises</div>
<div class="abs head title" style="top:2310px">Information About Cruises</div>
<div class="abs cruise-photo" role="img" aria-label="Crew members celebrating with a trophy"></div>
<div class="abs cruise-text">
  <p>The participants are consciously involved in sailing activities. There are responsibilities for a wide variety of tasks in daily life. A cooking and cleaning plan should help to take responsibility towards the group. The fact of steering a sailing ship alone fills many with great pride.</p>
  <p style="margin-top:29px">Recurring activities on the ship require the involvement of every crew member.</p>
</div>
<div class="abs thumb" style="left:589px;background:linear-gradient(180deg,#7fb5e0,#2a5fa8)" role="img" aria-label="Paddle board on the water"></div>
<div class="abs thumb" style="left:719px;background:linear-gradient(180deg,#c6a57c,#2c3650);border:4px solid #0094D4" role="img" aria-label="Crew members posing together"></div>
<div class="abs thumb" style="left:849px;background:linear-gradient(180deg,#a88b72,#4a3a35)" role="img" aria-label="Indoor group activity"></div>
<div class="abs thumb" style="left:979px;background:linear-gradient(180deg,#4aa0da,#17508f)" role="img" aria-label="Swimmers in the sea"></div>
<div class="abs track"><span></span></div>
<span class="abs btn" style="left:589px;top:2834px;background:var(--blue-2);font-size:24px;padding:10px 22px;box-shadow:0 4px 10px rgba(0,0,0,.2)">Learn More</span>

<!-- gallery -->
<div class="abs gallery" role="img" aria-label="Blue tinted photo of moored sailing masts"></div>
<div class="abs head ghost" style="top:3060px;color:rgba(255,255,255,.18)">Our Gallery</div>
<div class="abs head title" style="top:3096px;color:#fff">Our Gallery</div>
<div class="tile" style="left:111px;top:3170px;width:257px;height:280px;background:linear-gradient(160deg,#b58a5e,#5b3e2c)" role="img" aria-label="Award ceremony with trophy"></div>
<div class="tile" style="left:377px;top:3170px;width:256px;height:280px;background:linear-gradient(180deg,#6aa9d8,#3c7a4c 55%,#2d6fa6)" role="img" aria-label="Yachts anchored in a green bay"></div>
<div class="tile" style="left:643px;top:3170px;width:444px;height:280px;background:linear-gradient(180deg,#5f9bd2,#2660a8)" role="img" aria-label="Sailing yacht at sea"></div>
<div class="abs brand-box">
  <div class="name head">Sail Brightly</div>
  <div class="follow">Follow Us On: <span class="dot" style="width:24px;height:24px"></span><span class="dot" style="width:24px;height:24px"></span><span class="dot" style="width:24px;height:24px"></span></div>
</div>
<div class="tile" style="left:111px;top:3458px;width:236px;height:234px;background:linear-gradient(160deg,#a98a6c,#3f3a3c)" role="img" aria-label="Bowling night indoors"></div>
<div class="tile" style="left:358px;top:3458px;width:236px;height:234px;background:linear-gradient(160deg,#c2926c,#6a4e3c)" role="img" aria-label="Curling game indoors"></div>
<div class="tile" style="left:604px;top:3458px;width:237px;height:234px;background:linear-gradient(180deg,#4d9fd6,#1f6fae)" role="img" aria-label="Children on a paddle board"></div>
<div class="tile" style="left:851px;top:3458px;width:236px;height:234px;background:linear-gradient(180deg,#c94a4a,#55466a)" role="img" aria-label="Crowd at a charity run"></div>

<!-- sponsors -->
<div class="abs head ghost" style="top:3865px">Our Sponsors</div>
<div class="abs head title" style="top:3898px">Our Sponsors</div>
<p class="abs lead" style="top:3958px;left:200px;width:800px;font-size:15px">By <span class="hl">experiencing</span> a sailing week together, the "<span class="hl">Sail Brightly fleet</span>" creates ideal conditions under which the key objectives such as <span class="hl">social integration</span> and <span class="hl">educational development</span> of the children can be implemented in a <span class="hl">concrete, efficient</span> and <span class="hl">professional</span> manner and with a lasting effect.</p>
<div class="abs arrow dark" style="left:36px;top:4106px"><svg width="16" height="14" viewBox="0 0 16 14"><path d="M15 7H2M7 1L1 7l6 6" stroke="#222" stroke-width="2" fill="none"/></svg></div>
<div class="abs arrow dark" style="left:1130px;top:4106px"><svg width="16" height="14" viewBox="0 0 16 14"><path d="M1 7h13M9 1l6 6-6 6" stroke="#222" stroke-width="2" fill="none"/></svg></div>
<div class="abs sponsor" style="left:111px">Hartwald</div>
<div class="abs sponsor" style="left:364px">Brenner Bau</div>
<div class="abs sponsor on" style="left:618px">Lindmoor Reisen</div>
<div class="abs sponsor" style="left:873px">Volta Kramer</div>

<!-- footer -->
<svg class="abs" style="left:0;top:4236px" width="1200" height="100" viewBox="0 0 1200 100">
  <path d="M0 10 C300 90 700 100 1200 20 L1200 100 L0 100Z" fill="#7BADD7"/>
  <path d="M0 25 C300 95 700 100 1200 40 L1200 100 L0 100Z" fill="#0094D4"/>
  <path d="M0 40 C300 100 700 100 1200 58 L1200 100 L0 100Z" fill="#070d2c"/>
</svg>
<div class="abs footer"></div>
<div class="abs fcol" style="left:110px">
  <h5>Contact Us</h5>
  <ul>
    <li style="height:56px;align-items:flex-start"><span class="fcircle" style="flex:none"></span><span>Sail Brightly<br>United States</span></li>
    <li style="height:50px"><span class="fcircle"></span>info@sailbrightly.com</li>
    <li style="height:50px"><span class="fcircle"></span>+1 555 014 2290</li>
  </ul>
</div>
<div class="abs fcol" style="left:384px">
  <h5>Quick Links</h5>
  <ul><li><span class="chev">&raquo;</span>Home</li><li><span class="chev">&raquo;</span>About</li><li><span class="chev">&raquo;</span>Services</li><li><span class="chev">&raquo;</span>Contact Us</li></ul>
</div>
<div class="abs fcol" style="left:565px">
  <h5>Help Links</h5>
  <ul><li><span class="chev">&raquo;</span>FAQ</li><li><span class="chev">&raquo;</span>Sponsors</li><li><span class="chev">&raquo;</span>Privacy Policy</li><li><span class="chev">&raquo;</span>Terms &amp; Conditions</li></ul>
</div>
<div class="abs flogo">Sail<br>Brightly</div>
<p class="abs" style="left:902px;top:4475px;width:200px;font-size:14px;line-height:27px;color:#fff">The participants are consciously involved in sailing activities.</p>
<div class="abs" style="left:784px;top:4600px;display:flex;align-items:center;gap:22px;color:#fff;font-size:14px">Follow Us On: <span class="fcircle"></span><span class="fcircle"></span><span class="fcircle"></span></div>
<div class="abs" style="left:110px;top:4695px;width:977px;height:1px;background:rgba(255,255,255,.5)"></div>
<div class="abs" style="left:0;top:4730px;width:1200px;text-align:center;color:#fff;font-size:13px">Copyrights@2022.Sail Brightly.All Rights Reserved</div>

</body>
</html>
```